Refresh of The Marston Collective business card

Update business card design using existing primary logo. Names, numbers, etc. are too hard to read on current design.

Target Market(s)

We are a CPA firm.

Industry/Entity Type

Accountant

Contact Information for Business Card

update current card

Colors
0355a3
3176b5
85acd3
0792cd

Requirements
Must have
• Easier to read phone numbers and names
• Use existing logo
Nice to have
• We love our color scheme and current TMC logo. But the names and phone numbers are too small and card just look old and stale.

```html
<!DOCTYPE html>
<html lang="en">
<head>
<meta charset="utf-8">
<title>The Marston Collective – Business Card</title>
<link href="https://fonts.googleapis.com/css2?family=EB+Garamond:wght@400;600&display=swap" rel="stylesheet">
<style>
  :root {
    --navy: #0a2a6e;
    --primary: #0355a3;
    --mid: #3176b5;
    --light: #85acd3;
    --accent: #0792cd;
    --ink-dark: #1b2b4a;
    --paper: #ffffff;
    --paper-back: #f6f7fa;
    --stage: #4b4b4b;
    --rule: #3a5a9a;
  }
  * { box-sizing: border-box; margin: 0; padding: 0; }
  html, body { width: 1200px; height: 1200px; overflow: hidden; }
  body {
    background: var(--stage);
    font-family: "EB Garamond", Georgia, serif;
    display: flex;
    align-items: center;
    justify-content: center;
    gap: 40px;
  }
  .card {
    position: relative;
    width: 540px;
    height: 309px;
    overflow: hidden;
    box-shadow: 0 6px 18px rgba(0,0,0,.35);
  }

  /* Front */
  .card-front { background: var(--paper); }
  .front-header {
    position: absolute; inset: 0 0 auto 0; height: 124px;
    background: var(--paper);
    border-bottom: 7px solid var(--ink-dark);
  }
  .front-body {
    position: absolute; left: 0; right: 0; top: 124px; bottom: 0;
    background: radial-gradient(ellipse at 55% 40%, var(--mid) 0%, var(--primary) 40%, var(--navy) 100%);
  }
  .front-body .frame {
    position: absolute; left: 18px; right: 18px; bottom: 14px; height: 1px;
    background: rgba(133,172,211,.55);
  }
  .logo {
    display: flex; align-items: center; gap: 12px;
  }
  .logo-dot {
    width: 62px; height: 62px; border-radius: 50%;
    background: radial-gradient(circle at 40% 35%, var(--mid), var(--primary) 55%, var(--navy));
    flex: none;
  }
  .logo-text { display: flex; flex-direction: column; }
  .logo-name {
    color: var(--primary); font-weight: 600;
    font-size: 24px; line-height: 1.05; letter-spacing: .02em;
  }
  .logo-tag {
    color: var(--ink-dark); font-size: 8px; letter-spacing: .18em;
    text-transform: uppercase; margin-top: 4px;
    border-top: 1px solid var(--ink-dark); padding-top: 3px;
  }
  .front-header .logo { position: absolute; left: 26px; top: 28px; }
  .person-name {
    position: absolute; right: 24px; top: 150px;
    color: #fff; font-size: 23px; letter-spacing: .06em; text-transform: uppercase;
  }
  .contacts {
    position: absolute; left: 22px; top: 162px; list-style: none;
    color: #fff; font-size: 16px; line-height: 27px;
  }
  .contacts li { display: flex; align-items: center; gap: 9px; }
  .contacts svg { width: 14px; height: 14px; flex: none; }

  /* Back */
  .card-back { background: var(--paper-back); }
  .back-ring {
    position: absolute; width: 300px; height: 300px; left: 120px; top: 4px;
    border-radius: 50%; border: 14px solid rgba(133,172,211,.14);
    background: rgba(133,172,211,.07);
  }
  .rule { position: absolute; background: var(--rule); }
  .rule-tl-h { left: 0; top: 22px; width: 270px; height: 1px; }
  .rule-tl-v { left: 22px; top: 0; width: 1px; height: 190px; }
  .rule-br-h { right: 0; bottom: 22px; width: 270px; height: 1px; }
  .rule-br-v { right: 22px; bottom: 0; width: 1px; height: 190px; }
  .card-back .logo { position: absolute; left: 160px; top: 110px; }
  .back-web {
    position: absolute; left: 0; right: 0; top: 212px; text-align: center;
    color: var(--primary); font-size: 15px; font-weight: 600;
  }
</style>
</head>
<body>

<section class="card card-front" aria-label="Business card front">
  <div class="front-header">
    <div class="logo">
      <span class="logo-dot"></span>
      <div class="logo-text">
        <span class="logo-name">The Marston Collective</span>
        <span class="logo-tag">Certified Public Accountants</span>
      </div>
    </div>
  </div>
  <div class="front-body"><span class="frame"></span></div>
  <p class="person-name">Daniel R. Ashford, CPA</p>
  <ul class="contacts">
    <li><svg viewBox="0 0 14 14"><polygon points="7,0 13,3.5 13,10.5 7,14 1,10.5 1,3.5" fill="#1b2b4a" stroke="#85acd3" stroke-width=".8"/><rect x="4.5" y="3.5" width="5" height="7" rx="1" fill="#fff"/></svg>555.214.3870</li>
    <li><svg viewBox="0 0 14 14"><polygon points="7,0 13,3.5 13,10.5 7,14 1,10.5 1,3.5" fill="#1b2b4a" stroke="#85acd3" stroke-width=".8"/><path d="M4 9 L4 6 Q7 3.5 10 6 L10 9 Z" fill="#fff"/></svg>555.214.3871</li>
    <li><svg viewBox="0 0 14 14"><polygon points="7,0 13,3.5 13,10.5 7,14 1,10.5 1,3.5" fill="#1b2b4a" stroke="#85acd3" stroke-width=".8"/><rect x="4" y="4" width="6" height="6" fill="none" stroke="#fff" stroke-width="1"/></svg>555.862.1904</li>
    <li><svg viewBox="0 0 14 14"><polygon points="7,0 13,3.5 13,10.5 7,14 1,10.5 1,3.5" fill="#1b2b4a" stroke="#85acd3" stroke-width=".8"/><rect x="3.5" y="4.5" width="7" height="5" fill="#fff"/><path d="M3.5 4.5 L7 7.5 L10.5 4.5" stroke="#1b2b4a" stroke-width=".7" fill="none"/></svg>daniel@marstoncollective.com</li>
    <li><svg viewBox="0 0 14 14"><polygon points="7,0 13,3.5 13,10.5 7,14 1,10.5 1,3.5" fill="#1b2b4a" stroke="#85acd3" stroke-width=".8"/><circle cx="7" cy="7" r="3" fill="none" stroke="#fff" stroke-width="1"/><line x1="4" y1="7" x2="10" y2="7" stroke="#fff" stroke-width=".7"/></svg>www.marstoncollective.com</li>
  </ul>
</section>

<section class="card card-back" aria-label="Business card back">
  <span class="back-ring"></span>
  <span class="rule rule-tl-h"></span>
  <span class="rule rule-tl-v"></span>
  <span class="rule rule-br-h"></span>
  <span class="rule rule-br-v"></span>
  <div class="logo">
    <span class="logo-dot"></span>
    <div class="logo-text">
      <span class="logo-name">The Marston<br>Collective</span>
      <span class="logo-tag">Certified Public Accountants</span>
    </div>
  </div>
  <p class="back-web">www.marstoncollective.com</p>
</section>

</body>
</html>
```